Flyer-Design für private Musikakademie
Zielgruppe
Unsere Firma ist eine private Musikakademie für klassische Musik. Die Zielgruppe sind internationale Studenten und Publikum
Aufgabenstellung
Klassisch, elegant.
Wir benötigen einen Flyer im in zwei gefalteten A4 format (4 Seiten A5) für ein Festival in 2 Wochen.
Ausserdem benötigen wir einen stehenden Banner (ca. 2 m hoch) mit dem Hauptlogo und der Bezeichnung des Festivals.
Bitte kontaktieren Sie mich, falls Sie weiteres Bidmaterial, bzw. weitere Angaben benötigen. Das ist mein erstes aufgegebene Projekt hier.
Die Texteingabe ist in Deutsch/English. Meine Vorstellung wäre Deutsch etwas größer, English etwas versetzt darunter etwas kleiner, vielleicht kursiv, damit man es optisch gut auseinander halten kann

```html
<!DOCTYPE html>
<html lang="de">
<head>
<meta charset="utf-8">
<title>Music Academy Klangwerk Hannover – Flyer</title>
<link href="https://fonts.googleapis.com/css2?family=Bebas+Neue&family=Tinos:wght@400;700&display=swap" rel="stylesheet">
<style>
  :root {
    --teal-top: #2aafbd;
    --teal-mid: #20808a;
    --teal-deep: #16474f;
    --band-light: #d3e6e8;
    --ink-dark: #1a3e44;
    --accent: #2aa9b8;
    --white: #ffffff;
    --pink: #e0318a;
    --sponsor-yellow: #f3e23a;
  }
  * { box-sizing: border-box; margin: 0; padding: 0; }
  html, body { width: 1200px; height: 848px; overflow: hidden; }
  body {
    background: linear-gradient(180deg, var(--teal-top) 0%, var(--teal-mid) 50%, var(--teal-deep) 100%);
    font-family: "Tinos", "Times New Roman", serif;
    color: var(--white);
    position: relative;
  }
  .page {
    position: absolute;
    top: 27px;
    width: 550px;
    height: 794px;
    border: 4px solid var(--white);
  }
  .page--back { left: 26px; }
  .page--cover { left: 624px; }

  /* Back page */
  .band { position: absolute; left: 0; right: 0; text-align: center; }
  .band--donation { top: 0; height: 239px; padding-top: 34px; }
  .band--bank { top: 239px; height: 102px; background: var(--band-light); padding-top: 22px; }
  .band--receipt { top: 341px; height: 109px; padding-top: 19px; }
  .band--sponsor-title { top: 450px; height: 41px; background: var(--band-light); }
  .band--sponsors { top: 491px; height: 121px; display: flex; }
  .band--imprint { top: 612px; height: 126px; background: var(--teal-deep); display: flex; padding: 29px 0 0 34px; text-align: left; }
  .band--disclaimer { top: 738px; bottom: 0; background: var(--band-light); padding-top: 14px; }

  .heading {
    font-family: "Bebas Neue", "Arial Narrow", sans-serif;
    font-size: 27px;
    letter-spacing: 0.5px;
    color: var(--ink-dark);
    line-height: 1;
  }
  .band--sponsor-title .heading { line-height: 41px; font-size: 28px; }
  .body-copy {
    font-size: 11.5px;
    line-height: 18.3px;
    padding: 0 22px;
  }
  .body-copy + .body-copy { margin-top: 18px; }
  .band--donation .heading { margin-bottom: 16px; }

  .bank-line {
    font-family: "Bebas Neue", "Arial Narrow", sans-serif;
    font-size: 19.5px;
    line-height: 19px;
    color: var(--ink-dark);
  }
  .bank-line .label { color: var(--accent); }

  .sponsor {
    flex: 1;
    display: flex;
    align-items: center;
    justify-content: center;
    gap: 10px;
    font-family: "Tinos", "Times New Roman", serif;
  }
  .sponsor--bow { background: var(--white); color: var(--ink-dark); font-size: 26px; }
  .sponsor--friends { background: var(--pink); color: var(--sponsor-yellow); flex-direction: column; gap: 8px; font-size: 10px; }
  .sponsor--friends .sponsor-name { font-size: 22px; }
  .sponsor-square { width: 22px; height: 22px; background: #c4161c; }

  .imprint-col { font-size: 9px; line-height: 12px; }
  .imprint-col--address { width: 200px; }
  .imprint-col--manager { width: 150px; border-left: 1.5px solid var(--white); padding-left: 24px; height: 72px; }
  .imprint-col--editor { border-left: 1.5px solid var(--white); padding-left: 24px; height: 72px; }

  .disclaimer { font-size: 9px; line-height: 12.5px; color: var(--ink-dark); }

  /* Cover page */
  .brand {
    position: absolute;
    left: 0; right: 0;
    top: 60px;
    display: flex;
    flex-direction: column;
    align-items: center;
  }
  .brand-mark {
    width: 150px; height: 150px;
    border-radius: 50%;
    background: var(--white);
    margin-bottom: 90px;
  }
  .brand-name {
    font-family: "Bebas Neue", "Arial Narrow", sans-serif;
    color: var(--white);
    text-align: left;
    line-height: 0.95;
  }
  .brand-name span { display: block; }
  .brand-name .l1 { font-size: 38px; }
  .brand-name .l2 { font-size: 48px; }
  .brand-name .l3 { font-size: 58px; }

  .festival {
    position: absolute;
    left: 20px; right: 20px;
    top: 543px;
    height: 106px;
    border-top: 4px solid var(--white);
    border-bottom: 4px solid var(--white);
    text-align: center;
    font-family: "Bebas Neue", "Arial Narrow", sans-serif;
    font-size: 35px;
    line-height: 40px;
    padding-top: 8px;
    text-shadow: 2px 3px 4px rgba(0,0,0,0.35);
  }
  .site {
    position: absolute;
    left: 0; right: 0; top: 746px;
    text-align: center;
    font-size: 16px;
  }
</style>
</head>
<body>

<section class="page page--back">
  <div class="band band--donation">
    <h2 class="heading">Spendenkonto</h2>
    <p class="body-copy">Wir danken dem Verein FKKM e.V. für die grosszügige Unterstützung. Wenn Sie den FKKM Verein unterstützen möchten, um weitere Projekte ermöglichen zu können, freuen wir uns auf eine Spende. Jede Spende hilft uns und anderen Projekten, die von FKKM e.V. unterstützt werden.</p>
    <p class="body-copy">Bitte überweisen Sie Ihre Spende (Mindestbetrag 10€) auf folgende Kontonummer:</p>
    <p class="body-copy">Freunde klassischer Kunst und Musik e.V.</p>
  </div>

  <div class="band band--bank">
    <p class="bank-line"><span class="label">IBAN:</span> DE12500105170000123456</p>
    <p class="bank-line"><span class="label">BIC:</span> MUBKDE2HXXX</p>
    <p class="bank-line"><span class="label">Bank:</span> Musterbank Hannover</p>
  </div>

  <div class="band band--receipt">
    <p class="body-copy">Sie erhalten umgehend eine Spendenbescheinigung, wenn Sie uns eine Mail<br>mit Ihrem Namen, Ihrer Adresse, dem Spendenbetrag und einer Kopie<br>des Überweisungsbeleges an fkkm.ev@postfach.de senden.</p>
  </div>

  <div class="band band--sponsor-title">
    <h2 class="heading">Sponsored by</h2>
  </div>

  <div class="band band--sponsors">
    <div class="sponsor sponsor--bow">
      <span class="sponsor-square"></span>
      <span class="sponsor-name">Bogenhaus</span>
    </div>
    <div class="sponsor sponsor--friends">
      <span class="sponsor-name">FKKM</span>
      <span>Freunde klassischer Kunst und Musik e.V.</span>
    </div>
  </div>

  <div class="band band--imprint">
    <div class="imprint-col imprint-col--address">
      Music Academy Klangwerk Hannover<br>
      Am Lindenhof 14<br>
      30159 Hannover<br>
      Telefon:&nbsp; 0511-4412300<br>
      E-Mail:&nbsp;&nbsp; info@klangwerk-akademie.de<br>
      Internet: www.klangwerk-akademie.de
    </div>
    <div class="imprint-col imprint-col--manager">
      Geschäftsführer:<br>
      Konrad Albers<br>
      (Anschrift wie oben)<br>
      Steuer Nr. 21/204/5566<br>
      Steuer ID 40817263599
    </div>
    <div class="imprint-col imprint-col--editor">
      Inhaltlich Verantwortlicher<br>
      gemäß § 55 Abs. 2 RStV:<br>
      Konrad Albers<br>
      (Anschrift wie oben)
    </div>
  </div>

  <div class="band band--disclaimer">
    <p class="disclaimer">Haftungshinweis: Trotz sorgfältiger inhaltlicher Kontrolle übernehmen wir keine Haftung für die Inhalte externer Links.<br>Für den Inhalt der verlinkten Seiten sind ausschließlich deren Betreiber verantwortlich.</p>
  </div>
</section>

<section class="page page--cover">
  <div class="brand">
    <span class="brand-mark" aria-hidden="true"></span>
    <h1 class="brand-name">
      <span class="l1">Music Academy</span>
      <span class="l2">Klangwerk</span>
      <span class="l3">Hannover</span>
    </h1>
  </div>

  <div class="festival">
    1. Hannover-Klassik<br>
    International Festival and Competition
  </div>

  <p class="site">www.klangwerk-akademie.de</p>
</section>

</body>
</html>
```